Postcard Design

Baxley is a vip taxi and hire car service that specializes in airport to hotel transfers and surrounding suburbs at affordable rates . we offer a personalize service with over 40 years industry experience. we would like to promote a special from melbourne cbd to airport for $65 , our contact number is 0481926370, email primecabride@brisolmail.com , facebook orbit cab and rental car services we plan on distributing these flyers at all major hotels

Industry/Entity Type

Hotel

```html
<!DOCTYPE html>
<html lang="en">
<head>
<meta charset="utf-8">
<title>Orbit Cab and Rental Car Services – Postcards</title>
<link rel="stylesheet" href="https://fonts.googleapis.com/css2?family=Cinzel:wght@500;700&family=Arimo:wght@400;700&family=Tinos&display=swap">
<style>
  :root{
    --teal-dark:#0c2a3a;
    --teal:#1d4b62;
    --teal-mid:#2a5d76;
    --blue:#2f8fcf;
    --blue-deep:#1567a6;
    --white:#ffffff;
    --paper:#f4f5f6;
    --paper-shade:#c9ced2;
    --ink:#2b2f33;
    --grey:#7d8387;
    --grey-dark:#3c4145;
    --stage:#ebe8e4;
  }
  *{margin:0;padding:0;box-sizing:border-box}
  html,body{width:900px;height:1200px;overflow:hidden}
  body{background:var(--stage);position:relative;font-family:"Arimo",Arial,sans-serif}
  .postcard{position:absolute;left:120px;width:660px;height:470px;overflow:hidden;box-shadow:0 4px 14px rgba(0,0,0,.25)}
  .postcard--offer{top:90px}
  .postcard--classic{top:630px}
  .postcard svg.backdrop{position:absolute;inset:0;width:100%;height:100%}
  .brand-title{position:absolute;font-family:"Cinzel",serif;font-weight:700;color:var(--white);text-shadow:0 1px 2px rgba(0,0,0,.45);letter-spacing:.5px}

  /* offer card */
  .postcard--offer .brand-title{left:42px;top:14px;font-size:27px;white-space:nowrap}
  .offer-tagline{position:absolute;left:38px;top:55px;font-size:19px;color:var(--white)}
  .price-badge{position:absolute;left:48px;top:90px;width:122px;height:122px;border-radius:50%;background:radial-gradient(circle at 40% 30%,#5fb3e6,var(--blue-deep) 70%);border:5px solid var(--white);box-shadow:0 2px 6px rgba(0,0,0,.4);display:flex;align-items:center;justify-content:center;font-weight:700;font-size:46px;color:var(--white);z-index:2}
  .price-route{position:absolute;left:150px;top:106px;width:152px;height:50px;border-radius:25px;background:linear-gradient(#fff,#dfe3e6);box-shadow:0 1px 4px rgba(0,0,0,.35);font-weight:700;font-size:14px;line-height:16px;color:var(--ink);text-align:center;padding:8px 0 0 20px}
  .offer-details{position:absolute;left:22px;top:364px;color:var(--ink)}
  .offer-details .lead{font-size:17px}
  .offer-details .small{font-size:10px;margin-top:4px}
  .offer-details .rates{font-size:14px;font-weight:700;color:var(--blue-deep);letter-spacing:.5px;margin-top:3px}
  .social-line{display:flex;align-items:center;gap:8px;font-size:15px;color:var(--grey-dark)}
  .offer-details .social-line{margin-top:12px}
  .social-mark{width:13px;height:13px;background:var(--teal);display:inline-block}
  .contact{position:absolute;color:var(--grey-dark)}
  .contact .row{display:flex;align-items:center;gap:6px;font-size:12px;line-height:17px}
  .contact .phone{font-family:"Tinos",serif;font-size:25px;line-height:28px;color:var(--ink)}
  .contact svg{flex:none}
  .postcard--offer .contact{left:430px;top:366px}

  /* classic card */
  .postcard--classic .brand-title{left:0;width:480px;top:30px;font-size:36px;line-height:44px;text-align:center}
  .service-line{position:absolute;left:30px;top:165px;color:var(--white)}
  .service-line .a{font-size:30px}
  .service-line .b{font-size:23px;margin-top:6px}
  .service-line .c{font-size:37px;margin-top:2px}
  .contact-pill{position:absolute;left:0;top:318px;width:236px;height:88px;border-radius:0 44px 44px 0;background:linear-gradient(#fff,#d4d8db);box-shadow:0 2px 5px rgba(0,0,0,.35)}
  .postcard--classic .contact{left:30px;top:326px}
  .postcard--classic .social-line{position:absolute;right:30px;top:428px;color:var(--white);font-size:17px}
  .postcard--classic .social-mark{background:var(--white)}
</style>
</head>
<body>

<section class="postcard postcard--offer" aria-label="Postcard with airport offer">
  <svg class="backdrop" viewBox="0 0 660 470" preserveAspectRatio="none">
    <defs>
      <linearGradient id="offerTop" x1="0" y1="0" x2="0" y2="1">
        <stop offset="0" stop-color="#0f3346"/><stop offset="1" stop-color="#2a5d76"/>
      </linearGradient>
      <linearGradient id="offerBottom" x1="0" y1="0" x2="0" y2="1">
        <stop offset="0" stop-color="#ffffff"/><stop offset="1" stop-color="#c9ced2"/>
      </linearGradient>
      <linearGradient id="offerPhoto" x1="0" y1="0" x2="1" y2="1">
        <stop offset="0" stop-color="#b9c3c9"/><stop offset=".55" stop-color="#4a4f55"/><stop offset="1" stop-color="#1c1f23"/>
      </linearGradient>
    </defs>
    <rect width="660" height="470" fill="url(#offerBottom)"/>
    <path d="M0 0H660V70C560 80 470 100 380 125C250 165 120 200 0 190Z" fill="url(#offerTop)"/>
    <path d="M0 190C120 200 250 165 380 125C470 100 560 80 660 70V95C560 95 470 115 380 140C250 180 120 215 0 205Z" fill="#ffffff" opacity=".9"/>
    <path role="img" aria-label="Photo: chauffeur holding an umbrella beside a black limousine with a passenger, at an airport" d="M0 205C120 215 250 180 380 140C470 115 560 95 660 95V350C520 362 350 360 210 335C120 318 50 290 0 255Z" fill="url(#offerPhoto)"/>
    <path d="M0 255C50 290 120 318 210 335C350 360 520 362 660 350" fill="none" stroke="#1b4a63" stroke-width="14"/>
    <path d="M0 262C60 300 130 328 215 345C350 370 520 370 660 358" fill="none" stroke="#2f8fcf" stroke-width="5"/>
  </svg>
  <h1 class="brand-title">ORBIT CAB AND RENTAL CAR SERVICES</h1>
  <p class="offer-tagline">Specializes in Airport to Hotel Transfers</p>
  <div class="price-route">Melbourne cbd<br>to Airport</div>
  <div class="price-badge">$65</div>
  <div class="offer-details">
    <p class="lead">Specializes</p>
    <p class="small">in Airport to hotel Transfers and surrounding suburbs at</p>
    <p class="rates">AFFORDABLE RATES</p>
    <p class="social-line"><span class="social-mark"></span>Orbit-Cab-and-Rental-car-services</p>
  </div>
  <div class="contact">
    <p class="row phone"><svg width="13" height="13" viewBox="0 0 13 13"><rect width="13" height="13" rx="3" fill="#1d4b62"/><path d="M4 3l1.5 2-1 1c.5 1 1.5 2 2.5 2.5l1-1 2 1.5-1 1.5C6 10 3 7 2.5 4Z" fill="#fff"/></svg>0481926370</p>
    <p class="row"><svg width="13" height="10" viewBox="0 0 13 10"><rect width="13" height="10" rx="1" fill="#1d4b62"/><path d="M1 1l5.5 4.5L12 1" fill="none" stroke="#fff"/></svg>primecabride@brisolmail.com</p>
    <p class="row"><svg width="13" height="13" viewBox="0 0 13 13"><circle cx="6.5" cy="6.5" r="6" fill="#1d4b62"/><path d="M.5 6.5h12M6.5.5c-3 3-3 9 0 12M6.5.5c3 3 3 9 0 12" fill="none" stroke="#fff" stroke-width=".8"/></svg>www.orbitcabrental.com.au</p>
  </div>
</section>

<section class="postcard postcard--classic" aria-label="Postcard with car feature">
  <svg class="backdrop" viewBox="0 0 660 470" preserveAspectRatio="none">
    <defs>
      <linearGradient id="classicLeft" x1="0" y1="0" x2="1" y2="1">
        <stop offset="0" stop-color="#1d4b62"/><stop offset="1" stop-color="#0c2a3a"/>
      </linearGradient>
      <radialGradient id="classicRight" cx=".65" cy=".5" r=".6">
        <stop offset="0" stop-color="#f2f3f4"/><stop offset="1" stop-color="#8e9397"/>
      </radialGradient>
      <linearGradient id="classicCar" x1="0" y1="0" x2="0" y2="1">
        <stop offset="0" stop-color="#8c9196"/><stop offset=".6" stop-color="#43484d"/><stop offset="1" stop-color="#25282b"/>
      </linearGradient>
    </defs>
    <rect width="660" height="470" fill="url(#classicLeft)"/>
    <path d="M620 0H660V470H210C270 400 290 320 340 240C410 130 520 50 620 0Z" fill="url(#classicRight)"/>
    <path d="M640 30C520 80 410 150 330 250C290 300 265 360 240 420" fill="none" stroke="#2f8fcf" stroke-width="9"/>
    <path d="M660 50C540 95 425 170 345 265" fill="none" stroke="#d5d9dc" stroke-width="4"/>
    <rect role="img" aria-label="Photo: dark grey sedan, three-quarter front view" x="255" y="220" width="380" height="175" rx="60" fill="url(#classicCar)" opacity=".9"/>
  </svg>
  <h1 class="brand-title">ORBIT CAB AND RENTAL<br>CAR SERVICES</h1>
  <div class="service-line">
    <p class="a">Specializes in</p>
    <p class="b">Airport to Hotel</p>
    <p class="c">Transfers</p>
  </div>
  <div class="contact-pill"></div>
  <div class="contact">
    <p class="row phone"><svg width="13" height="13" viewBox="0 0 13 13"><rect width="13" height="13" rx="3" fill="#1d4b62"/><path d="M4 3l1.5 2-1 1c.5 1 1.5 2 2.5 2.5l1-1 2 1.5-1 1.5C6 10 3 7 2.5 4Z" fill="#fff"/></svg>0481926370</p>
    <p class="row"><svg width="13" height="10" viewBox="0 0 13 10"><rect width="13" height="10" rx="1" fill="#1d4b62"/><path d="M1 1l5.5 4.5L12 1" fill="none" stroke="#fff"/></svg>primecabride@brisolmail.com</p>
    <p class="row"><svg width="13" height="13" viewBox="0 0 13 13"><circle cx="6.5" cy="6.5" r="6" fill="#1d4b62"/><path d="M.5 6.5h12M6.5.5c-3 3-3 9 0 12M6.5.5c3 3 3 9 0 12" fill="none" stroke="#fff" stroke-width=".8"/></svg>www.orbitcabrental.com.au</p>
  </div>
  <p class="social-line">Orbit-Cab-and-Rental-car-services<span class="social-mark"></span></p>
</section>

</body>
</html>
```